Business card design for global fintech startup

Veltrix is a modern payments platform for the global insurance industry, serving international health, life, and travel insurers, MGAs, brokers, and partners.

We need a professional, premium business card for use at insurance conferences and executive meetings. The goal is to create a card that feels trustworthy, modern, and high-quality, while still being distinctive and memorable in a stack of business cards.

Target audience:
Senior insurance executives (VP, C-suite).

Design goals:
Clear, professional, and credible
Modern but not trendy
Premium and well-structured
Easy to read and practical for networking

Brand direction:
Brand-first (company over individual)
Follow existing brand guidelines where possible
Clean layout, strong hierarchy, excellent readability

Must include:
Name
Title
Company name (Veltrix)
Logo
Email
Phone/Whatsapp
Website (www.withveltrix.example)
Tagline - Clarity in every payment

Materials & finish:
Open to designer recommendations for premium look and feel.

Please avoid:
Flashy or trendy startup styles
Generic insurance icons or clichés
Cluttered layouts or hard-to-read text

Deliverables:
Front and back business card, print-ready files.

Target Market(s)

Global Insurance executives

Industry/Entity Type

Fintech, Insurtech, Insurance, Financial Services

Contact Information for Business Card

Name Title Company name (Veltrix) Logo Email Phone/Whatsapp Website (www.withveltrix.example) Tagline - Clarity in every payment

Font styles to use
Other font styles liked:
• See brand guidelines

Requirements
Nice to have
• something that stands out/makes us more memorable while still remaining professional
Should not have
• Please avoid: Flashy or trendy startup styles Generic insurance icons or clichés Cluttered layouts or hard-to-read text

```html
<!DOCTYPE html>
<html lang="en">
<head>
<meta charset="UTF-8">
<title>Veltrix Business Card</title>
<link rel="stylesheet" href="https://fonts.googleapis.com/css2?family=Poppins:wght@400;500;600;700&display=swap">
<style>
  :root {
    --stage: #1c1c1c;
    --card: #0b0b0b;
    --facet-light: #1d1d1d;
    --facet-dark: #050505;
    --ink: #ffffff;
    --ink-soft: #e6e6e6;
    --rule: #bdbdbd;
  }
  * { box-sizing: border-box; margin: 0; padding: 0; }
  html, body {
    width: 1200px; height: 1200px; overflow: hidden;
    background: var(--stage);
    font-family: "Poppins", sans-serif;
    color: var(--ink);
  }
  .canvas {
    width: 1200px; height: 1200px;
    display: flex; flex-direction: column; align-items: center; justify-content: center;
    gap: 44px;
  }
  .card {
    position: relative;
    width: 900px; height: 514px;
    background: var(--card);
    box-shadow: 0 18px 40px rgba(0,0,0,.55);
    overflow: hidden;
  }
  .card-texture {
    position: absolute; inset: 0;
    background:
      linear-gradient(135deg, rgba(255,255,255,.04) 0%, rgba(0,0,0,0) 45%),
      linear-gradient(160deg, var(--facet-light) 0%, var(--card) 55%, var(--facet-dark) 100%);
  }
  .card-content { position: relative; width: 100%; height: 100%; }

  /* Front */
  .front .card-content {
    display: flex; flex-direction: column; align-items: center; justify-content: center;
  }
  .brand-name {
    font-weight: 600;
    font-size: 92px;
    letter-spacing: 10px;
    line-height: 1;
    color: var(--ink);
    text-transform: uppercase;
  }
  .tagline {
    margin-top: 26px;
    font-weight: 400;
    font-size: 15px;
    letter-spacing: 12px;
    text-transform: uppercase;
    color: var(--ink-soft);
  }

  /* Back */
  .identity {
    position: absolute; right: 500px; top: 170px;
    text-align: right;
  }
  .person-name {
    font-weight: 700; font-size: 32px; letter-spacing: 1px;
    text-transform: uppercase; line-height: 1.1;
  }
  .person-title {
    font-weight: 400; font-size: 26px; line-height: 1.15; color: var(--ink-soft);
  }
  .divider {
    position: absolute; left: 425px; top: 160px;
    width: 1.5px; height: 112px; background: var(--rule);
  }
  .contact-list {
    position: absolute; left: 460px; top: 170px;
    list-style: none;
    display: flex; flex-direction: column; gap: 8px;
  }
  .contact-item {
    display: flex; align-items: center; gap: 14px;
    font-size: 24px; font-weight: 400; line-height: 1.2;
  }
  .contact-icon { width: 20px; height: 20px; flex: none; }
  .address {
    position: absolute; left: 60px; bottom: 78px;
    font-size: 25px; font-weight: 400; color: var(--ink-soft);
  }
</style>
</head>
<body>
<main class="canvas">
  <section class="card front">
    <div class="card-texture" role="img" aria-label="Faceted dark triangle texture across the card face"></div>
    <div class="card-content">
      <h1 class="brand-name">Veltrix</h1>
      <p class="tagline">Clarity in every payment</p>
    </div>
  </section>

  <section class="card back">
    <div class="card-texture" role="img" aria-label="Faceted dark triangle texture across the card face"></div>
    <div class="card-content">
      <div class="identity">
        <h2 class="person-name">Daniel R. Hayes</h2>
        <p class="person-title">Founder</p>
      </div>
      <div class="divider"></div>
      <ul class="contact-list">
        <li class="contact-item">
          <svg class="contact-icon" viewBox="0 0 24 24" aria-hidden="true"><path fill="#fff" d="M6.6 10.8a15.1 15.1 0 0 0 6.6 6.6l2.2-2.2a1 1 0 0 1 1-.25 11.4 11.4 0 0 0 3.6.57 1 1 0 0 1 1 1V20a1 1 0 0 1-1 1A17 17 0 0 1 3 4a1 1 0 0 1 1-1h3.5a1 1 0 0 1 1 1c0 1.250.2 2.45.57 3.57a1 1 0 0 1-.25 1z"/></svg>
          <span>+1 555-010-2040</span>
        </li>
        <li class="contact-item">
          <svg class="contact-icon" viewBox="0 0 24 24" aria-hidden="true"><rect x="2" y="5" width="20" height="14" fill="#fff"/><path d="M2 5l10 8 10-8" fill="none" stroke="#0b0b0b" stroke-width="1.6"/></svg>
          <span>info@veltrixmail.example</span>
        </li>
        <li class="contact-item">
          <svg class="contact-icon" viewBox="0 0 24 24" aria-hidden="true"><g fill="none" stroke="#fff" stroke-width="1.6"><circle cx="12" cy="12" r="9.5"/><ellipse cx="12" cy="12" rx="4.2" ry="9.5"/><path d="M2.5 12h19M4 7h16M4 17h16"/></g></svg>
          <span>www.withveltrix.example</span>
        </li>
      </ul>
      <p class="address">4820 Harbor Park Dr 2nd floor, Denver CO 80216, United States</p>
    </div>
  </section>
</main>
</body>
</html>
```